Beacon Advisory Website

I currently have a website www.beaconadvisoryinc.example. We are a IT Consulting Company. Our website will pretty much tell out our services. I am looking to enhance my website and make it look more professional. Looking for very classy and Contemporary look and design for my website.

Industry/Entity Type

It Company

```html
<!DOCTYPE html>
<html lang="en">
<head>
<meta charset="utf-8">
<title>Beacon Advisory</title>
<link href="https://fonts.googleapis.com/css2?family=Open+Sans:wght@400;600;700&family=Roboto+Condensed:wght@400;700&display=swap" rel="stylesheet">
<style>
:root{
  --blue:#1a9bd7;
  --blue-dark:#1485bb;
  --ink:#333;
  --muted:#666;
  --light-gray:#e2e2e2;
  --footer:#585858;
  --footer-bottom:#3a3a3a;
  --white:#fff;
}
*{box-sizing:border-box;margin:0;padding:0}
html,body{width:1200px;height:2799px;overflow:hidden}
body{position:relative;font-family:"Open Sans",Arial,sans-serif;color:var(--ink);background:var(--white)}
.abs{position:absolute}

/* header */
.site-header{position:absolute;top:0;left:0;width:1200px;height:80px;background:rgba(255,255,255,.96);z-index:3}
.brand{position:absolute;left:132px;top:22px;display:flex;align-items:center;gap:10px}
.brand-mark{width:34px;height:34px;background:var(--blue)}
.brand-name{font-size:19px;font-weight:700;color:var(--blue-dark)}
.main-nav{position:absolute;left:460px;top:0;height:80px;display:flex;align-items:center;gap:18px;font-size:11.5px;font-weight:600;color:#222}
.main-nav .active{color:var(--blue)}
.social-bar{position:absolute;right:0;top:0;width:295px;height:80px;background:var(--blue);display:flex;align-items:center;padding-left:34px;gap:14px}
.social-dot{width:14px;height:14px;border-radius:50%;background:var(--white)}

/* hero */
.hero{position:absolute;left:0;top:0;width:1200px;height:578px;background:linear-gradient(90deg,#eef1f3 0%,#e3e8ec 30%,#b9c6d2 55%,#c7d3de 75%,#e6ebef 100%)}
.hero-copy{position:absolute;left:132px;top:216px}
.hero-title{font-family:"Roboto Condensed",Arial,sans-serif;font-size:29px;font-weight:700;color:var(--blue);margin-bottom:14px}
.hero-list{list-style:none}
.hero-list li{display:flex;align-items:center;gap:14px;font-size:13px;color:#222;height:31px}
.hero-list svg{width:14px;height:14px}
.btn{display:inline-block;background:var(--blue);color:var(--white);font-size:11px;font-weight:600;text-transform:uppercase;padding:0 18px;height:29px;line-height:29px}
.hero .btn{margin-top:16px}
.slider-arrow{position:absolute;top:300px;width:33px;height:34px;background:#3c3c3c;display:flex;align-items:center;justify-content:center}
.slider-dots{position:absolute;left:570px;top:556px;display:flex;gap:4px}
.slider-dots span{width:17px;height:4px;background:#555}
.slider-dots .on{background:var(--blue)}

/* section headings */
.section-title{position:absolute;left:0;width:1200px;display:flex;justify-content:center;align-items:center;font-size:25px;color:#444}
.section-title b{font-weight:700;color:var(--blue);border-left:1px solid #999;padding-left:12px;margin-left:12px;line-height:44px}

/* about */
.about{position:absolute;left:0;top:602px;width:1200px;height:388px;background:var(--light-gray)}
.about-photo{position:absolute;left:165px;top:36px;width:305px;height:352px;background:linear-gradient(180deg,#d0d0d0,#7e7e7e 60%,#5a5a5a)}
.about-copy{position:absolute;left:604px;top:92px;width:466px}
.about-copy h2{font-size:25px;font-weight:400;color:#444;display:flex;align-items:center}
.about-copy h2 b{color:var(--blue);border-left:1px solid #999;padding-left:10px;margin-left:10px;line-height:40px}
.about-copy p{font-size:11px;line-height:19px;color:#555;margin:18px 0 24px}

/* services */
.service{position:absolute;width:300px;display:flex;gap:24px}
.service-icon{flex:none;width:56px;height:56px;background:#444;display:flex;align-items:center;justify-content:center}
.service-icon.featured{background:var(--blue)}
.service h3{font-size:15.5px;font-weight:400;color:#333;margin:-2px 0 8px}
.service p{font-size:10.5px;line-height:14px;color:#555}
.service.featured h3,.service.featured p{color:var(--blue)}

/* team */
.team{position:absolute;left:0;top:1380px;width:1200px;height:261px;display:flex}
.team-member{width:300px;height:261px;position:relative}
.team-overlay{position:absolute;left:112px;top:108px;display:flex;gap:4px}
.team-overlay span{width:38px;height:38px;background:var(--white);display:flex;align-items:center;justify-content:center}

/* testimonials */
.testimonials{position:absolute;left:0;top:1750px;width:1200px;height:468px;background:var(--blue)}
.quote-card{position:absolute;top:66px;width:297px;height:334px;background:var(--white);text-align:center}
.quote-avatar{width:94px;height:94px;border-radius:50%;margin:25px auto 0;background:radial-gradient(circle,#d6b9a3,#a99a8e);border:3px solid #eee}
.quote-mark{font-family:Georgia,serif;font-size:40px;color:#ccc;line-height:30px;margin-top:14px}
.quote-text{font-size:13px;font-weight:600;line-height:17px;color:#222;padding:0 28px;margin-top:4px}
.quote-author{font-size:12px;color:var(--blue);margin-top:10px}

/* clients */
.clients{position:absolute;left:224px;top:2325px;width:778px;height:186px;display:grid;grid-template-columns:repeat(5,1fr);grid-template-rows:repeat(2,1fr)}
.client{display:flex;align-items:center;justify-content:center;border-right:1px solid #eee;border-bottom:1px solid #eee;font-size:27px;font-weight:600;color:#b8b8b8}
.client:nth-child(5n){border-right:none}
.client:nth-child(n+6){border-bottom:none}
.client.featured{color:#222}

/* footer */
.site-footer{position:absolute;left:0;top:2537px;width:1200px;height:198px;background:var(--footer);color:#eee}
.footer-col{position:absolute;top:30px}
.footer-col h4{font-size:13px;font-weight:400;margin-bottom:16px}
.footer-col h4 b{font-weight:700;border-left:1px solid #bbb;padding-left:7px;margin-left:5px}
.footer-col p,.footer-col li{font-size:9.5px;line-height:20px;color:#ddd;list-style:none}
.links{display:flex;gap:30px}
.feed-item{display:flex;gap:10px;margin-bottom:6px}
.feed-dot{flex:none;width:8px;height:8px;border-radius:50%;background:#ddd;margin-top:6px}
.newsletter-input{width:215px;height:29px;background:#ddd;font-size:9px;color:#888;padding:8px 10px}
.newsletter .btn{margin-top:13px;height:28px;line-height:28px;padding:0 25px;font-size:9px}
.footer-bottom{position:absolute;left:0;top:2735px;width:1200px;height:64px;background:var(--footer-bottom)}
.copyright{position:absolute;left:132px;top:26px;font-size:9.5px;color:#aaa}
.footer-social{position:absolute;right:132px;top:25px;display:flex;gap:16px}
.footer-social span{width:13px;height:13px;border-radius:50%;background:#888}
</style>
</head>
<body>

<section class="hero" role="img" aria-label="Photo of three colleagues gathered around a tablet in a bright office">
  <div class="hero-copy">
    <h1 class="hero-title">We offer a wide range of skill levels</h1>
    <ul class="hero-list">
      <li><svg viewBox="0 0 14 14"><circle cx="7" cy="7" r="7" fill="#222"/><path d="M5.5 4l3 3-3 3" stroke="#fff" stroke-width="1.6" fill="none"/></svg>Internet and Enabling Technologies</li>
      <li><svg viewBox="0 0 14 14"><circle cx="7" cy="7" r="7" fill="#222"/><path d="M5.5 4l3 3-3 3" stroke="#fff" stroke-width="1.6" fill="none"/></svg>Enterprise Resource Planning (ERP)</li>
      <li><svg viewBox="0 0 14 14"><circle cx="7" cy="7" r="7" fill="#222"/><path d="M5.5 4l3 3-3 3" stroke="#fff" stroke-width="1.6" fill="none"/></svg>Product Engineering</li>
      <li><svg viewBox="0 0 14 14"><circle cx="7" cy="7" r="7" fill="#222"/><path d="M5.5 4l3 3-3 3" stroke="#fff" stroke-width="1.6" fill="none"/></svg>Data Warehousing/ Business Intelligence</li>
    </ul>
    <a class="btn">Read More</a>
  </div>
  <div class="slider-arrow" style="left:16px"><svg width="10" height="12" viewBox="0 0 10 12"><path d="M7 1L2 6l5 5" stroke="#fff" stroke-width="1.8" fill="none"/></svg></div>
  <div class="slider-arrow" style="right:16px"><svg width="10" height="12" viewBox="0 0 10 12"><path d="M3 1l5 5-5 5" stroke="#fff" stroke-width="1.8" fill="none"/></svg></div>
  <div class="slider-dots"><span class="on"></span><span></span><span></span></div>
</section>

<header class="site-header">
  <div class="brand"><span class="brand-mark"></span><span class="brand-name">Beacon Advisory</span></div>
  <nav class="main-nav">
    <span class="active">COMPANY</span><span>SERVICES</span><span>SOLUTIONS</span><span>RESOURCES</span><span>CAREER</span><span>CONTACT US</span>
  </nav>
  <div class="social-bar"><span class="social-dot"></span><span class="social-dot"></span><span class="social-dot"></span><span class="social-dot"></span></div>
</header>

<section class="about">
  <div class="about-photo" role="img" aria-label="Photo of three business professionals in suits"></div>
  <div class="about-copy">
    <h2>About <b>The Company</b></h2>
    <p>Today's IT market is a dynamic, fast-paced industry, with ever-increasing demands. Meeting these demands for over 25 years, Beacon Advisory maintains a global presence, aggressively recruiting expertly qualified IT and Management Professionals from around the world and cultivating key partnerships with corporations to understand their business models end-to-end, with a goal of delivering exceptional client service and ensuring a consistent delivery of the talent needed to drive results.</p>
    <a class="btn">Read More</a>
  </div>
</section>

<h2 class="section-title" style="top:1015px">Our Amazing <b>Services</b></h2>

<div class="service featured" style="left:127px;top:1120px">
  <div class="service-icon featured"><svg width="30" height="30" viewBox="0 0 30 30" fill="#fff"><circle cx="9" cy="8" r="4"/><circle cx="21" cy="8" r="4"/><rect x="3" y="14" width="24" height="4"/><rect x="6" y="20" width="4" height="8"/><rect x="20" y="20" width="4" height="8"/></svg></div>
  <div><h3>Consulting</h3><p>Beacon Advisory has certified profes-sional consultants to work with you to help increase the business by providing</p></div>
</div>
<div class="service" style="left:447px;top:1120px">
  <div class="service-icon"><svg width="30" height="30" viewBox="0 0 30 30" fill="#fff"><circle cx="15" cy="9" r="5"/><circle cx="7" cy="13" r="3.5"/><circle cx="23" cy="13" r="3.5"/><path d="M7 27c0-6 4-10 8-10s8 4 8 10z"/></svg></div>
  <div><h3>Staff Augmentation</h3><p>For years Beacon Advisory as been offer-ing our customers the ability to augment their existing staff</p></div>
</div>
<div class="service" style="left:767px;top:1120px">
  <div class="service-icon"><svg width="30" height="30" viewBox="0 0 30 30" fill="none" stroke="#fff" stroke-width="3"><circle cx="11" cy="17" r="5"/><circle cx="22" cy="9" r="3.5"/></svg></div>
  <div><h3>Offshore</h3><p>Our Offshore development model has a unique distinction of providing efficient software solutions</p></div>
</div>
<div class="service" style="left:127px;top:1224px">
  <div class="service-icon"><svg width="30" height="30" viewBox="0 0 30 30" stroke="#fff" stroke-width="4" stroke-linecap="round"><path d="M6 24L20 10"/><path d="M8 7l15 16"/></svg></div>
  <div><h3>Fully Customizable</h3><p>Curabitur id quam et lacus interdise lacu-lis vitae ets nisi. Varius loremis feugiat, aliquam et massa nulla.</p></div>
</div>
<div class="service" style="left:447px;top:1224px">
  <div class="service-icon"><svg width="26" height="26" viewBox="0 0 26 26" fill="#fff"><rect x="1" y="1" width="11" height="11"/><rect x="14" y="1" width="11" height="11"/><rect x="1" y="14" width="11" height="11"/><rect x="14" y="14" width="11" height="11"/></svg></div>
  <div><h3>Unlimited Options</h3><p>Curabitur id quam et lacus interdise lacu-lis vitae ets nisi. Varius loremis feugiat, aliquam et massa nulla.</p></div>
</div>
<div class="service" style="left:767px;top:1224px">
  <div class="service-icon"><svg width="32" height="30" viewBox="0 0 32 30" fill="none" stroke="#fff" stroke-width="2"><rect x="2" y="3" width="28" height="19"/><path d="M6 17l6-6 5 4 7-8"/><path d="M12 27h8"/></svg></div>
  <div><h3>SEO Ready</h3><p>Curabitur id quam et lacus interdise lacu-lis vitae ets nisi. Varius loremis feugiat, aliquam et massa nulla.</p></div>
</div>

<h2 class="section-title" style="top:1309px">Our <b>Team</b></h2>

<section class="team">
  <div class="team-member" role="img" aria-label="Portrait of a smiling team member" style="background:linear-gradient(135deg,#c9c9c9,#8d7f75)"></div>
  <div class="team-member" role="img" aria-label="Portrait of a team member, highlighted on hover" style="background:linear-gradient(135deg,#2e2e2e,#5a5049)">
    <div class="team-overlay">
      <span><svg width="16" height="16" viewBox="0 0 16 16" stroke="#1a9bd7" stroke-width="2" fill="none"><path d="M2 14L14 2M9 2h5v5M2 9v5h5"/></svg></span>
      <span><svg width="16" height="16" viewBox="0 0 16 16" stroke="#1a9bd7" stroke-width="2" fill="none"><rect x="2" y="6" width="7" height="5" rx="2.5" transform="rotate(-45 5.5 8.5)"/><rect x="7" y="5" width="7" height="5" rx="2.5" transform="rotate(-45 10.5 7.5)"/></svg></span>
    </div>
  </div>
  <div class="team-member" role="img" aria-label="Portrait of a smiling team member" style="background:linear-gradient(135deg,#9a9a9a,#6d625a)"></div>
  <div class="team-member" role="img" aria-label="Portrait of a smiling team member" style="background:linear-gradient(135deg,#d8d6d3,#a99480)"></div>
</section>

<h2 class="section-title" style="top:1670px">Client <b>Testimonials</b></h2>

<section class="testimonials">
  <div class="quote-card" style="left:131px">
    <div class="quote-avatar" role="img" aria-label="Client portrait"></div>
    <div class="quote-mark">&ldquo;</div>
    <p class="quote-text">Lorem ipsum dolor sit amet, consectetur adipiscing elit. Maecenas a eros mollis, blandit ligula eu, euismod magna. Vivamus ultricies est ac dolor ultricies, id hendrerit quam vulputate.</p>
    <p class="quote-author">-Alex Moran</p>
    <div class="quote-mark">&ldquo;</div>
  </div>
  <div class="quote-card" style="left:451px">
    <div class="quote-avatar" role="img" aria-label="Client portrait"></div>
    <div class="quote-mark">&ldquo;</div>
    <p class="quote-text">Lorem ipsum dolor sit amet, consectetur adipiscing elit. Maecenas a eros mollis, blandit ligula eu, euismod magna. Vivamus ultricies est ac dolor ultricies, id hendrerit quam vulputate.</p>
    <p class="quote-author">-Alex Moran</p>
    <div class="quote-mark">&ldquo;</div>
  </div>
  <div class="quote-card" style="left:771px">
    <div class="quote-avatar" role="img" aria-label="Client portrait"></div>
    <div class="quote-mark">&ldquo;</div>
    <p class="quote-text">Lorem ipsum dolor sit amet, consectetur adipiscing elit. Maecenas a eros mollis, blandit ligula eu, euismod magna. Vivamus ultricies est ac dolor ultricies, id hendrerit quam vulputate.</p>
    <p class="quote-author">-Alex Moran</p>
    <div class="quote-mark">&ldquo;</div>
  </div>
</section>

<h2 class="section-title" style="top:2240px">Our <b>Clients</b></h2>

<div class="clients">
  <div class="client">Meridian</div><div class="client">Meridian</div><div class="client featured">Meridian</div><div class="client">Meridian</div><div class="client">Meridian</div>
  <div class="client">Meridian</div><div class="client">Meridian</div><div class="client">Meridian</div><div class="client">Meridian</div><div class="client">Meridian</div>
</div>

<footer class="site-footer">
  <div class="footer-col" style="left:132px;width:215px">
    <h4>About<b>Company</b></h4>
    <p>Today's IT market is a dynamic, fast-paced industry, with ever-increasing demands. Meeting these demands for over 25 years, Beacon Advisory maintains a global presence, aggressively recruiting expertly qualified IT and Management Professionals</p>
  </div>
  <div class="footer-col" style="left:373px">
    <h4>Quick<b>Link</b></h4>
    <div class="links">
      <ul><li>Our Company</li><li>Monthly Statistics</li><li>Our Services</li><li>FAQ &amp; Help Center</li><li>Login with account</li></ul>
      <ul><li>Our Philosophy</li><li>Marketing Strategies</li><li>Support Forums</li><li>Register an account</li><li>Careers</li></ul>
    </div>
  </div>
  <div class="footer-col" style="left:610px;width:210px">
    <h4>Social<b>Feed</b></h4>
    <div class="feed-item"><span class="feed-dot"></span><p>@Beacon Advisory&nbsp; Creating a new theme for information Technology. #12 mins ago</p></div>
    <div class="feed-item"><span class="feed-dot"></span><p>@Beacon Advisory&nbsp; Creating a new theme for information Technology. #12 mins ago</p></div>
  </div>
  <div class="footer-col newsletter" style="left:852px">
    <h4>Suscribe<b>Newsletter</b></h4>
    <div class="newsletter-input">Enter your email</div>
    <a class="btn">Subscribe</a>
  </div>
</footer>

<div class="footer-bottom">
  <p class="copyright">Copyright &copy; &nbsp;Beacon Advisory . All Rights Reserved</p>
  <div class="footer-social"><span></span><span></span><span></span><span></span></div>
</div>

</body>
</html>
```